International wholefood supplement business requires product label design for supplement product.

We are a whole food supplement business specializing in native plant nutrition. We need a product label designed for our natural whole food vitamin C product. We have developed this product from the organic wild-harvested Australian Kakadu Plum. The brand is ZEVRA.
1. Label Size: 135mm X 45mm
2. Brand is ZEVRA and slogan is Pure Roots Bright Days.
3. It is ok to choose you own color and font. However, at a later stage, I will present the product in a presentation box containing charcoal (Hex #333333) matte gold (Hex: #CBAB58)and orange (Hex #FF6600) colors, so please keep this in mind when choosing your colors. How you blend the colors into the white color of the bottle is up to you.
4. I do like the see-through panels with the Kakadu Plum image on the old label, although I would also like to see designs without this.
5. Logo; I have attached the logo png file for you to use. I will provide the winner with the .eps or .ai files to complete their final design.
6. Layout as you want; however, the words “NO THERAPEUTIC CLAIMS” must remain where they are and must be in black bold font.
7. Finished label must include Bleed and Cut Marks.
8. I require the finished label design print-ready files and source files.
9. I have included an image of Kakadu Plums for your use if needed.
10. You must also supply a finished mock-up of the label on the bottle.
11. Bottle size 84mm high x 45mm diameter with a 40mm diameter cap.
12. I require all vector files and source files.

For label wording please see my full brief attached.

Target Market(s)

My market is the 30-75-year-old male and female customers concerned with good health.

Industry/Entity Type

Health Product

Requirements
Must have
• A finished mock-up of the label on the bottle.
A fresh new design that is not too similar to my old label. Please be creative.
I would like to see designs using orange, charcoal and gold or silver and designers ow choice of colors.
A bespoke upmarket design.
Nice to have
• It is ok to choose you own color and font. However, at a later stage, I will present the product in a presentation box containing charcoal (Hex #333333) matte gold (Hex: #CBAB58)and orange (Hex #FF6600) colors, so please keep this in mind when choosing your colors. How you blend the colors into the white color of the bottle is up to you.

```html
<!DOCTYPE html>
<html lang="en">
<head>
<meta charset="utf-8">
<title>ZEVRA Kakadu Plum Label</title>
<link rel="stylesheet" href="https://fonts.googleapis.com/css2?family=Lato:wght@300;400;700&family=Montserrat:wght@700&family=Oswald:wght@300;400&display=swap">
<style>
  :root {
    --orange-deep: #C2461A;
    --orange: #EE5F21;
    --orange-text: #F15A1F;
    --peach: #F4884F;
    --peach-soft: #F6A87A;
    --gold: #C9A55C;
    --gold-light: #D9BF80;
    --charcoal: #333333;
    --grey: #4a4a4a;
    --white: #ffffff;
    --backdrop: #e6e6e6;
  }
  * { box-sizing: border-box; margin: 0; padding: 0; }
  html, body { width: 1200px; height: 1200px; overflow: hidden; }
  body { background: var(--backdrop); font-family: "Lato", sans-serif; position: relative; }

  .label {
    position: absolute; left: 30px; top: 410px;
    width: 1140px; height: 381px;
    background: var(--white);
    overflow: hidden;
    box-shadow: 0 2px 10px rgba(0,0,0,0.12);
  }
  .label > * { position: absolute; }

  .top-band {
    left: 0; top: 0; width: 100%; height: 166px;
    background: linear-gradient(90deg, var(--orange-deep) 0%, var(--orange) 50%, var(--orange-deep) 100%);
  }
  .gold-stripe {
    left: 0; top: 166px; width: 100%; height: 10px;
    background: linear-gradient(90deg, var(--gold) 0%, var(--gold-light) 50%, var(--gold) 100%);
  }

  .provenance {
    left: 31px; top: 16px; width: 317px; height: 127px;
    background: var(--peach);
    color: #1e1e1e; font-size: 21px; line-height: 28.5px;
    text-align: center; padding-top: 6px;
  }

  .brand {
    left: 440px; top: 20px; width: 260px;
    display: flex; flex-direction: column; align-items: center;
  }
  .brand-name {
    display: flex; align-items: center; gap: 8px;
    color: var(--gold-light); font-size: 42px; font-weight: 400; letter-spacing: 2px; line-height: 44px;
  }
  .brand-dot { width: 18px; height: 18px; border-radius: 50%; background: var(--gold-light); }
  .brand-slogan {
    color: var(--gold-light); font-size: 7.5px; letter-spacing: 1.6px; text-transform: uppercase; margin-top: 1px;
  }

  .product-name {
    left: 408px; top: 83px; width: 300px;
    color: var(--white); font-weight: 300; font-size: 45px; letter-spacing: 0.5px; white-space: nowrap;
  }
  .product-tagline {
    left: 410px; top: 135px;
    color: var(--peach-soft); font-weight: 300; font-size: 17px; white-space: nowrap;
  }

  .description {
    left: 798px; top: 26px; width: 305px;
    color: var(--white); font-size: 16px; line-height: 24px; letter-spacing: 0.6px;
    text-align: justify; text-align-last: justify;
  }

  .checklist {
    font-family: "Oswald", sans-serif; font-weight: 300; font-size: 18px;
    color: var(--grey); white-space: nowrap; text-transform: uppercase;
  }
  .checklist::before { content: "\2713\00a0 "; font-family: "Lato", sans-serif; }
  .check-organic { left: 52px; top: 187px; }
  .check-eco { left: 207px; top: 187px; }
  .check-wild { left: 52px; top: 212px; }
  .check-sustainable { left: 207px; top: 212px; }
  .check-fair { left: 124px; top: 239px; }

  .contact-box {
    left: 76px; top: 272px; width: 220px; height: 68px;
    border: 1.5px solid var(--gold); border-radius: 10px;
    text-align: center; color: #111; font-size: 20px; line-height: 28px; padding-top: 4px;
  }

  .batch, .expiry { top: 347px; color: var(--grey); font-size: 17px; }
  .batch { left: 14px; }
  .expiry { left: 238px; }

  .badges { left: 413px; top: 187px; width: 200px; height: 58px; }
  .plum-photo-frame { left: 628px; top: 155px; width: 115px; height: 115px; }

  .origin {
    left: 480px; top: 276px; width: 200px; text-align: center;
    color: var(--grey); font-size: 21px; letter-spacing: 0.6px;
  }
  .flag { left: 560px; top: 311px; width: 42px; height: 21px; }

  .no-claims {
    left: 400px; top: 350px; width: 335px; text-align: center;
    font-family: "Montserrat", sans-serif; font-weight: 700; font-size: 18px; color: #000; letter-spacing: 0.4px;
  }

  .vitamin-claim {
    left: 810px; top: 186px; width: 275px; text-align: center;
    color: var(--orange-text); font-weight: 700; font-size: 19px; line-height: 25px;
  }

  .spec-box {
    left: 798px; width: 44px;
    border: 1.5px solid var(--gold);
    color: var(--gold); text-align: center; font-family: "Oswald", sans-serif;
  }
  .spec-box .spec-num { display: block; font-size: 22px; line-height: 26px; font-weight: 400; }
  .spec-box .spec-unit { display: block; font-size: 7px; line-height: 10px; border-top: 1px solid var(--gold); }
  .spec-capsules { top: 270px; height: 45px; }
  .spec-weight { top: 321px; height: 46px; }

  .spec-text {
    left: 854px; font-family: "Oswald", sans-serif; font-weight: 300; font-size: 19px;
    color: #222; line-height: 28px; white-space: nowrap;
  }
  .spec-text-capsules { top: 272px; }
  .spec-text-weight { top: 316px; }
</style>
</head>
<body>
  <div class="label">
    <div class="top-band"></div>
    <div class="gold-stripe"></div>

    <div class="provenance">Harvested by<br>Australian indigenous peoples.<br>Authenticated by<br>elders of the land.</div>

    <div class="brand">
      <div class="brand-name"><span class="brand-dot"></span>ZEVRA</div>
      <div class="brand-slogan">Pure Roots Bright Days</div>
    </div>

    <div class="product-name">KAKADU PLUM</div>
    <div class="product-tagline">Sourced from Pristine Wilderness</div>

    <p class="description">The Kakadu plum fruit contains a unique combination of Hypophillic and Lipophilic antioxidants, organic compounds, micro-nutrients, vitamins and minerals in their natural form.</p>

    <div class="checklist check-organic">Organic</div>
    <div class="checklist check-eco">Eco-friendly</div>
    <div class="checklist check-wild">Wild harvested</div>
    <div class="checklist check-sustainable">Sustainable</div>
    <div class="checklist check-fair">Fair trade</div>

    <div class="contact-box">Wattle Grove Health<br>www.wattlegrove.health</div>

    <div class="batch">Batch No. 888001</div>
    <div class="expiry">Exp. No: 01/21</div>

    <svg class="badges" viewBox="0 0 200 58" aria-hidden="true">
      <circle cx="28" cy="29" r="25" fill="none" stroke="var(--gold)" stroke-width="2.5"/>
      <circle cx="100" cy="29" r="25" fill="none" stroke="var(--gold)" stroke-width="2.5"/>
      <circle cx="172" cy="29" r="25" fill="none" stroke="var(--gold)" stroke-width="2.5"/>
    </svg>

    <svg class="plum-photo-frame" viewBox="0 0 115 115" role="img" aria-label="Photograph of green Kakadu plums on a stem">
      <defs>
        <radialGradient id="plumFill" cx="45%" cy="40%" r="60%">
          <stop offset="0%" stop-color="#b9c46a"/>
          <stop offset="60%" stop-color="#8a9a3e"/>
          <stop offset="100%" stop-color="#f4f4ec"/>
        </radialGradient>
      </defs>
      <circle cx="57.5" cy="57.5" r="54" fill="url(#plumFill)" stroke="var(--gold)" stroke-width="3.5"/>
    </svg>

    <div class="origin">Product of Australia</div>
    <svg class="flag" viewBox="0 0 42 21" role="img" aria-label="Australian flag">
      <rect width="42" height="21" fill="#1f2f6e"/>
      <rect width="18" height="10" fill="#c8273a" opacity="0.85"/>
    </svg>

    <div class="no-claims">NO THERAPEUTIC CLAIMS</div>

    <div class="vitamin-claim">Contains the highest natural vitamin C content of any fruit or vegetable.</div>

    <div class="spec-box spec-capsules"><span class="spec-num">30</span><span class="spec-unit">CAPSULES</span></div>
    <div class="spec-text spec-text-capsules">30 vegetable Capsules per bottle</div>

    <div class="spec-box spec-weight"><span class="spec-num">250</span><span class="spec-unit">MG</span></div>
    <div class="spec-text spec-text-weight">250mg of pure Kakadu Plum<br>fruit powder in each capsule</div>
  </div>
</body>
</html>
```